MORU-TEK vegan protein

Hi
We need a vegan protein label and logo for our company
MORU-TEK
We made a quick sketch in the type of way we want it But you can always make it better
Dont mind the logo we sketched please come up with something else
Left side of the label please the color of the taste So brown red vanille we need 3 designs for Chocolate, strawberry and vanilla
Backside: leave nutrition faces blank,
One square text with: Pea Protein derived and extracted from organic grean split peas. It is a great source of fiber (helps with digestion and less bloating), vitamines and minerals. Studies have shown that the intake of pea protein can reduce high blood pressure and that it can be used for prevention and controll of diabetes as it has minimal effect on blood glucose levels and insulin response.
One square with suggested use:
Add 1 or 2 scoops to a blender, shaker or glass with cold water or your favorite beverage (various amount of liquid to achieve your desired taste). Shake or mix well before consumption.
Distributed by:
DRAVEN COMPANY BV
THE NETHERLANDS
Please make it look amazing elegant and premium elite looking
It will be made on a alu bag like a send In the pictures

```html
<!DOCTYPE html>
<html lang="en">
<head>
<meta charset="utf-8">
<title>MORU-TEK Organic Vegan Protein – Chocolate</title>
<link href="https://fonts.googleapis.com/css2?family=Oswald:wght@500;600&family=Roboto:wght@500;700;900&display=swap" rel="stylesheet">
<style>
  :root{
    --canvas:#ededed;
    --foil:#f4f4f4;
    --cocoa:#5a3a22;
    --cocoa-light:#8a5a36;
    --leaf:#3b8a3f;
    --leaf-dark:#2e6a33;
    --ink:#1f1f1f;
    --white:#ffffff;
  }
  *{box-sizing:border-box;margin:0;padding:0}
  html,body{width:1200px;height:1078px;overflow:hidden;background:var(--canvas)}
  .label{
    position:absolute;left:332px;top:131px;width:516px;height:820px;
    background:var(--foil);overflow:hidden;
    font-family:"Roboto",Arial,sans-serif;
  }
  .label__bands{position:absolute;inset:0}
  .brand-vertical{
    position:absolute;left:101px;top:428px;
    transform:translate(-50%,-50%) rotate(-90deg) scaleX(.85);
    font-family:"Oswald",Arial,sans-serif;font-weight:600;
    font-size:104px;line-height:1;color:var(--white);white-space:nowrap;
  }
  .brand-vertical__reg{
    position:absolute;left:32px;top:190px;font-size:15px;color:var(--white);
  }
  .flavour-photo{
    position:absolute;left:61px;top:682px;width:90px;height:90px;border-radius:50%;
    background:radial-gradient(circle at 50% 55%,var(--cocoa-light) 0 30%,#c9a689 45%,#f6f6f6 62%);
  }
  .title{
    position:absolute;left:130px;width:400px;text-align:center;
    font-family:"Oswald",Arial,sans-serif;font-weight:500;color:var(--leaf);line-height:1;
    transform:scaleX(.88);transform-origin:center;
  }
  .title--top{top:166px;font-size:55px}
  .title--bottom{top:217px;font-size:55px}
  .wordmark{
    position:absolute;left:190px;top:328px;width:290px;
    display:flex;align-items:center;justify-content:center;gap:12px;
  }
  .wordmark__square{width:26px;height:26px;background:var(--leaf-dark)}
  .wordmark__name{
    font-family:"Oswald",Arial,sans-serif;font-weight:600;font-size:52px;line-height:1;color:var(--leaf-dark);
  }
  .leaf-art{
    position:absolute;left:295px;top:460px;width:80px;height:44px;
    background:linear-gradient(90deg,#5aa646,#3b8a3f);border-radius:0 40px 0 40px;
  }
  .claim{
    position:absolute;left:180px;width:310px;text-align:center;
    font-weight:900;color:var(--leaf-dark);line-height:1;
  }
  .claim--pct{top:511px;font-size:26px}
  .claim--text{top:542px;font-size:27px}
  .badge{
    position:absolute;width:68px;height:68px;border-radius:50%;
    background:var(--cocoa);border:2px solid var(--foil);box-shadow:0 0 0 1.5px var(--cocoa);
    color:var(--white);display:flex;flex-direction:column;align-items:center;justify-content:center;
    line-height:1;text-align:center;
  }
  .badge__big{font-weight:700;font-size:24px}
  .badge__big small{font-size:14px}
  .badge__big--gf{font-size:27px}
  .badge__small{font-weight:500;font-size:11px;margin-top:2px}
  .badge__stack{font-weight:500;font-size:10px;line-height:1.15}
  .net-weight{
    position:absolute;left:232px;top:761px;width:200px;text-align:center;
    font-weight:700;font-size:17px;color:var(--ink);
  }
  .net-weight b{font-size:22px}
</style>
</head>
<body>
<main class="label">
  <svg class="label__bands" viewBox="0 0 516 820" width="516" height="820" aria-hidden="true">
    <rect x="0" y="41" width="516" height="7" fill="var(--cocoa)"/>
    <rect x="0" y="57" width="516" height="4" fill="var(--cocoa)"/>
    <path d="M0 82 L4 78 L8 82 L12 78 L16 82 L20 78 L24 82 L28 78 L32 82 L36 78 L40 82 L44 78 L48 82 L52 78 L56 82 L60 78 L64 82 L68 78 L72 82 L76 78 L80 82 L84 78 L88 82 L92 78 L96 82 L100 78 L104 82 L108 78 L112 82 L116 78 L120 82 L124 78 L128 82 L132 78 L136 82 L140 78 L144 82 L148 78 L152 82 L156 78 L162 82 L165 80 L165 792 Q330 812 516 790 L516 820 L0 820 Z" fill="var(--cocoa)"/>
  </svg>

  <div class="brand-vertical">MORU - TEK</div>
  <span class="brand-vertical__reg">®</span>
  <div class="flavour-photo" role="img" aria-label="Photo of chocolate pieces for the chocolate flavour"></div>

  <h1 class="title title--top">ORGANIC</h1>
  <h2 class="title title--bottom">VEGAN PROTEIN</h2>

  <div class="wordmark">
    <span class="wordmark__square"></span>
    <span class="wordmark__name">MORU-TEK</span>
  </div>

  <div class="leaf-art" role="img" aria-label="Green leaf illustration"></div>
  <p class="claim claim--pct">100%</p>
  <p class="claim claim--text">PLANT BASED</p>

  <div class="badge" style="left:186px;top:630px;z-index:1"><span class="badge__big">0</span><span class="badge__small">Sugars</span></div>
  <div class="badge" style="left:247px;top:621px;z-index:2"><span class="badge__big">7<small>g</small></span><span class="badge__small">Organic</span></div>
  <div class="badge" style="left:305px;top:633px;z-index:3"><span class="badge__big">21<small>g</small></span><span class="badge__small">Protein</span></div>
  <div class="badge" style="left:364px;top:619px;z-index:5"><span class="badge__big badge__big--gf">GF</span></div>
  <div class="badge" style="left:416px;top:624px;z-index:4"><span class="badge__stack">Super<br>Food<br>Vitamins</span></div>

  <p class="net-weight">Net.Wt.<b>700gr</b></p>
</main>
</body>
</html>
```